Korvex Systems*

Stationary design including business cards, letter heads, envelops and email signatures using our new logo

Target Market(s)

Innovative Technologies

Industry/Entity Type

Defense Contracting

Font styles to use
Sans Serif

```html
<!DOCTYPE html>
<html lang="en">
<head>
<meta charset="utf-8">
<title>Korvex Systems — Stationery</title>
<link href="https://fonts.googleapis.com/css2?family=Barlow+Condensed:wght@400;500&family=Barlow+Semi+Condensed:wght@400;600&family=Arimo:wght@400&display=swap" rel="stylesheet">
<style>
:root{
  --board:#7b7b7b;
  --paper:#ffffff;
  --ink:#1c1c1e;
  --text:#555559;
  --rule:#d9d9d9;
}
*{margin:0;padding:0;box-sizing:border-box}
html,body{width:1200px;height:699px;overflow:hidden;background:var(--board)}
.board{position:relative;width:1200px;height:699px}
.piece{position:absolute;background:var(--paper);box-shadow:0 1px 3px rgba(0,0,0,.35)}
.wordmark{font-family:"Barlow Condensed",sans-serif;font-weight:500;letter-spacing:.02em;white-space:nowrap;color:var(--ink)}
.contact{font-family:"Barlow Semi Condensed",sans-serif;font-weight:400}
.contact-list{list-style:none}
.contact-list li{display:flex;align-items:center;gap:3px}
.icon{width:5px;height:5px;flex:none;fill:currentColor}

/* business card front */
.card-front{left:72px;top:320px;width:243px;height:138px;display:flex}
.card-front .brand-side{width:118px;display:flex;align-items:center;justify-content:center}
.card-front .brand-side .wordmark{font-size:16px}
.card-front .info-side{flex:1;background:var(--ink);color:#fff;padding:32px 0 0 20px}
.person-name{font-family:"Barlow Semi Condensed",sans-serif;font-weight:600;font-size:8.5px;letter-spacing:.03em;line-height:1}
.person-role{font-size:5.6px;margin:2px 0 6px}
.card-front .address{font-size:5.4px;line-height:6.9px;margin-bottom:5px}
.card-front .contact-list li{font-size:5.4px;line-height:6.9px}

/* business card back */
.card-back{left:72px;top:494px;width:243px;height:138px;background:var(--ink);display:flex;align-items:center;justify-content:center}
.card-back .wordmark{color:#fff;font-size:20px;margin-top:20px}

/* letterhead */
.letterhead{left:344px;top:59px;width:406px;height:574px}
.letterhead .head{position:absolute;top:89px;left:0;right:0;text-align:center}
.letterhead .head .wordmark{font-size:15px}
.letter-body{position:absolute;left:34px;top:160px;width:340px;font-family:"Arimo",sans-serif;color:var(--text)}
.greeting{font-size:9px;margin-bottom:17px}
.letter-body p{font-size:5px;line-height:8.2px;text-align:justify;margin-bottom:9px}
.signoff{margin-top:14px}
.signature{margin-top:8px;width:106px;height:22px;background:linear-gradient(90deg,#eeeeee,#f6f6f6)}
.letter-footer{position:absolute;left:0;right:0;bottom:0;height:40px;background:var(--ink);color:#fff;text-align:center;font-size:6.6px;padding-top:8px}
.letter-footer .row{display:flex;justify-content:center;align-items:center;gap:4px}
.letter-footer hr{border:0;border-top:.6px solid #ddd;width:290px;margin:3px auto 4px}

/* email signature */
.email-sig{left:782px;top:194px;width:333px;height:85px}
.email-sig .brand{position:absolute;left:14px;top:48px}
.email-sig .brand .wordmark{font-size:10px}
.email-sig .divider{position:absolute;top:20px;width:.8px;height:35px;background:var(--ink)}
.email-sig .who{position:absolute;left:110px;top:19px;color:var(--ink)}
.email-sig .who .person-name{font-size:10px}
.email-sig .who .person-role{font-size:6.6px;margin:1px 0 4px}
.email-sig .who .address{font-size:6.3px;line-height:8px}
.email-sig .contact-list{position:absolute;left:236px;top:20px;color:var(--ink)}
.email-sig .contact-list li{font-size:6.4px;line-height:8.1px}
.email-sig .band{position:absolute;left:0;right:0;bottom:0;height:15px;background:var(--ink);color:#fff;font-size:6.6px;letter-spacing:.14em;text-align:center;line-height:15px}

/* envelope back */
.envelope-back{left:783px;top:308px;width:330px;height:147px;background:#fbfbfb}
.envelope-back svg{position:absolute;inset:0}
.envelope-back .wordmark{position:absolute;left:0;right:0;top:36px;text-align:center;color:#fff;font-size:8px}

/* envelope front */
.envelope-front{left:780px;top:485px;width:333px;height:149px}
.envelope-front .brand{position:absolute;left:16px;top:51px}
.envelope-front .brand .wordmark{font-size:10px}
.envelope-front .band{position:absolute;left:0;right:0;bottom:0;height:28px;background:var(--ink);color:#fff;text-align:center;font-size:6.5px;line-height:7.8px;padding-top:6px}
</style>
</head>
<body>
<div class="board">

  <section class="piece card-front">
    <div class="brand-side"><span class="wordmark">KORVEX SYSTEMS</span></div>
    <div class="info-side contact">
      <div class="person-name">DANIEL REYES</div>
      <div class="person-role">President</div>
      <div class="address">Korvex Systems LLC<br>2210 Larkspur Way<br>Juneau, Alaska 99801</div>
      <ul class="contact-list">
        <li><svg class="icon" viewBox="0 0 10 10"><path d="M2 0l2 2-1 2 3 3 2-1 2 2-2 2C4 10 0 6 0 2z"/></svg>555-214-0186</li>
        <li><svg class="icon" viewBox="0 0 10 10"><path d="M2 0h6v10H2zM3 1v7h4V1z"/></svg>555-318-0427</li>
        <li><svg class="icon" viewBox="0 0 10 10"><path d="M2 0h6v3H2zM0 3h10v5H8v2H2V8H0z"/></svg>555-406-0953</li>
        <li><svg class="icon" viewBox="0 0 10 10"><path d="M0 2h10v6H0zM1 3l4 3 4-3z"/></svg>info@korvexsystems.com</li>
        <li><svg class="icon" viewBox="0 0 10 10"><circle cx="5" cy="5" r="5"/></svg>www.korvexsystems.com</li>
      </ul>
    </div>
  </section>

  <section class="piece card-back"><span class="wordmark">KORVEX SYSTEMS</span></section>

  <section class="piece letterhead">
    <div class="head"><span class="wordmark">KORVEX SYSTEMS</span></div>
    <div class="letter-body">
      <div class="greeting">Dear Mr. Reyes,</div>
      <p>Lorem ipsum dolor sit amet, consectetur adipiscing elit. Donec orci purus, luctus vitae dignissim eu, iaculis sed purus. Vivamus faucibus, ipsum nec aliquet viverra, leo mauris condimentum ligula, sit amet sagittis enim ligula quis arcu. Nam egestas tortor id nisi porttitor mattis. In tortor ante, ultricies in suscipit a, tempus non massa. Vivamus et auctor mi. Fusce vel massa nulla. Phasellus nec eros mauris, et scelerisque orci.</p>
      <p>Donec malesuada orci vitae nulla accumsan porta a id massa. Quisque accumsan iaculis magna sit amet fringilla. Maecenas consequat, magna eget tincidunt semper, odio nibh rutrum mi, id feugiat ante nisi eu risus. Vestibulum nunc orci, rhoncus a placerat in, ultricies in mi. Cras mattis varius eros, vel fringilla nisi suscipit eget. Quisque scelerisque sagittis nulla at porttitor.</p>
      <p>Sed id augue vitae urna euismod commodo aliquet a quam. Pellentesque arcu velit, cursus et malesuada ut, consequat et diam. Nullam erat sem, rhoncus id ullamcorper vitae, rhoncus et arcu. In ultricies ultricies nulla, ut rutrum nisi iaculis at. Donec eu magna a metus ornare faucibus. Fusce aliquet faucibus ultricies. Morbi semper, est id tincidunt gravida, sem arcu adipiscing lacus, ac bibendum nulla leo eu purus. Quisque nec diam sed risus consectetur a accumsan quis quis nibh. Vestibulum id purus lorem.</p>
      <p>It is a long established fact that a reader will be distracted by the readable content of a page when looking at its layout. The point of using Lorem Ipsum is that it has a more-or-less normal distribution of letters, as opposed to using 'Content here, content here', making it look like readable English. Many desktop publishing packages</p>
      <p>ada ut, consequat et diam. Nullam erat sem, rhoncus id ullamcorper vitae, rhoncus et arcu. In ultricies ultricies nulla, ut rutrum nisi iaculis at. Donec eu magna a metus ornare faucibus. Fusce aliquet faucibus ultricies. Morbi semper,</p>
      <p class="signoff">Sincerely,</p>
      <div class="signature" role="img" aria-label="Handwritten signature"></div>
    </div>
    <footer class="letter-footer contact">
      <div class="row"><svg class="icon" viewBox="0 0 10 10"><path d="M5 0a3.5 3.5 0 0 1 3.5 3.5C8.5 6 5 10 5 10S1.5 6 1.5 3.5A3.5 3.5 0 0 1 5 0z"/></svg>Korvex Systems LLC | 2210 Larkspur Way | Juneau, Alaska 99801</div>
      <hr>
      <div class="row">
        <svg class="icon" viewBox="0 0 10 10"><path d="M2 0l2 2-1 2 3 3 2-1 2 2-2 2C4 10 0 6 0 2z"/></svg>555-214-0186
        <svg class="icon" viewBox="0 0 10 10"><path d="M2 0h6v10H2zM3 1v7h4V1z"/></svg>555-318-0427
        <svg class="icon" viewBox="0 0 10 10"><path d="M2 0h6v3H2zM0 3h10v5H8v2H2V8H0z"/></svg>555-406-0953
        <svg class="icon" viewBox="0 0 10 10"><path d="M0 2h10v6H0zM1 3l4 3 4-3z"/></svg>info@korvexsystems.com
        <svg class="icon" viewBox="0 0 10 10"><circle cx="5" cy="5" r="5"/></svg>www.korvexsystems.com
      </div>
    </footer>
  </section>

  <section class="piece email-sig contact">
    <div class="brand"><span class="wordmark">KORVEX SYSTEMS</span></div>
    <div class="divider" style="left:89px"></div>
    <div class="who">
      <div class="person-name">DANIEL REYES</div>
      <div class="person-role">President</div>
      <div class="address">2210 Larkspur Way<br>Juneau, Alaska 99801</div>
    </div>
    <div class="divider" style="left:217px"></div>
    <ul class="contact-list">
      <li><svg class="icon" viewBox="0 0 10 10"><path d="M2 0l2 2-1 2 3 3 2-1 2 2-2 2C4 10 0 6 0 2z"/></svg>555-214-0186</li>
      <li><svg class="icon" viewBox="0 0 10 10"><path d="M2 0h6v10H2zM3 1v7h4V1z"/></svg>555-318-0427</li>
      <li><svg class="icon" viewBox="0 0 10 10"><path d="M2 0h6v3H2zM0 3h10v5H8v2H2V8H0z"/></svg>555-406-0953</li>
      <li><svg class="icon" viewBox="0 0 10 10"><path d="M0 2h10v6H0zM1 3l4 3 4-3z"/></svg>info@korvexsystems.com</li>
    </ul>
    <div class="band">www.korvexsystems.com</div>
  </section>

  <section class="piece envelope-back">
    <svg viewBox="0 0 330 147" preserveAspectRatio="none">
      <path d="M2 145 L150 60 M328 145 L180 60" stroke="#e6e6e6" stroke-width=".8" fill="none"/>
      <path d="M0 0 H330 L320 14 L190 82 Q165 95 140 82 L10 14 Z" fill="var(--ink)"/>
    </svg>
    <span class="wordmark">KORVEX SYSTEMS</span>
  </section>

  <section class="piece envelope-front contact">
    <div class="brand"><span class="wordmark">KORVEX SYSTEMS</span></div>
    <div class="band">Korvex Systems LLC<br>2210 Larkspur Way, Juneau, Alaska 99801</div>
  </section>

</div>
</body>
</html>
```